Brightwell Bonds and Households Initiative

We need a flyer that invites low-income Spanish speaking individuals to our program. The program is 12 weeks. We offer healthy relationship education, and financial stability. We also touch on workforce development. These workshops are for couples only.

We are in five locations, so we need a flyer that we can change the text to be able to update the address, dates and any additional information based on our needs.

Attached is the logo we would like to use. I have also attached a previous flyer that we created to give you an idea of the text that is included.

Target Market(s)

We are reaching out to low income adult couples

Font styles to use
Serif

Requirements
Must have
• This flyer must catch the eye of couples wanting to improve their relationship, and finances.
Nice to have
• Some space for us to plug in dates location and times. This flyer also has to have our funding statement at the bottom.

```html
<!DOCTYPE html>
<html lang="es">
<head>
<meta charset="utf-8">
<title>Talleres para Parejas</title>
<link href="https://fonts.googleapis.com/css2?family=Bebas+Neue&family=Open+Sans:wght@400;600;700&display=swap" rel="stylesheet">
<style>
  :root {
    --navy: #2c3757;
    --gold: #c98b2b;
    --orange: #e98f26;
    --ink: #4a4a4a;
    --white: #ffffff;
    --photo-light: #ece7df;
    --photo-mid: #c9b9a3;
  }
  * { margin: 0; padding: 0; box-sizing: border-box; }
  html, body { width: 902px; height: 1200px; overflow: hidden; background: var(--white); }
  body { font-family: "Open Sans", sans-serif; color: var(--ink); }
  .flyer { position: relative; width: 902px; height: 1200px; background: var(--white); }

  .brand { position: absolute; top: 36px; left: 0; width: 902px; text-align: center; }
  .brand-mark { display: inline-block; width: 22px; height: 22px; border-radius: 50%; background: var(--orange); margin-bottom: 14px; }
  .brand-name { font-weight: 600; font-size: 23px; color: var(--orange); line-height: 1.2; }

  .hero-photo { position: absolute; top: 150px; left: 0; width: 902px; height: 313px;
    background: linear-gradient(180deg, var(--white) 0%, var(--photo-light) 30%, var(--photo-mid) 100%); }

  .headline-band { position: absolute; top: 463px; left: 0; width: 902px; height: 135px; background: var(--navy); text-align: center; color: var(--white); }
  .headline { font-family: "Bebas Neue", sans-serif; font-weight: 400; font-size: 66px; letter-spacing: 1px; line-height: 1; margin-top: 17px; }
  .subhead { font-weight: 700; font-size: 21px; line-height: 28px; margin-top: 2px; }

  .details { position: absolute; top: 598px; left: 0; width: 902px; height: 181px; }
  .detail { position: absolute; top: 26px; text-align: center; font-weight: 600; font-size: 16.5px; line-height: 19px; }
  .detail-label { display: table; margin: 0 auto 16px; background: var(--navy); color: var(--white); font-weight: 400; font-size: 17.5px; line-height: 36px; height: 36px; padding: 0 20px; border-radius: 11px; }
  .detail-dates { left: 107px; width: 200px; }
  .detail-time { left: 399px; width: 160px; }
  .detail-place { left: 594px; width: 280px; }
  .note { position: absolute; top: 133px; left: 134px; font-weight: 600; font-size: 16px; }

  .topics { position: absolute; top: 779px; left: 0; width: 453px; height: 301px; background: var(--gold); color: var(--white); }
  .topics h2 { font-weight: 700; font-size: 24px; line-height: 30px; margin: 40px 0 0 121px; }
  .topics ul { list-style: none; width: 360px; margin: 9px 0 0 56px; font-weight: 600; font-size: 16.5px; line-height: 18.8px; }
  .topics li { position: relative; padding-left: 28px; }
  .topics li::before { content: "•"; position: absolute; left: 0; }

  .register { position: absolute; top: 779px; left: 453px; width: 449px; height: 301px; background: var(--navy); color: var(--white); text-align: center; }
  .register-call { font-size: 30px; line-height: 37px; margin-top: 72px; }
  .register-info { font-size: 18px; line-height: 20.5px; margin-top: 34px; }

  .footer { position: absolute; top: 1080px; left: 0; width: 902px; height: 120px; }
  .partner { position: absolute; top: 40px; font-weight: 700; font-size: 12px; line-height: 14px; text-align: center; color: var(--orange); }
  .partner-resource { left: 50px; width: 170px; }
  .partner-alliance { left: 232px; width: 165px; color: var(--navy); }
  .partner-dot { display: block; width: 14px; height: 14px; margin: 0 auto 5px; border-radius: 50%; background: currentColor; }
  .funding { position: absolute; top: 38px; left: 414px; width: 455px; text-align: center; font-weight: 600; font-size: 11px; line-height: 13.6px; }
</style>
</head>
<body>
<main class="flyer">
  <header class="brand">
    <span class="brand-mark"></span>
    <div class="brand-name">Brightwell Bonds and Households Initiative</div>
  </header>

  <div class="hero-photo" role="img" aria-label="Foto de una familia de tres generaciones sonriendo en un sofá"></div>

  <section class="headline-band">
    <h1 class="headline">TALLERES PARA PAREJAS</h1>
    <p class="subhead">Porque una relación sana esta “En Nuestras Manos”</p>
  </section>

  <section class="details">
    <div class="detail detail-dates">
      <span class="detail-label">Fecha de talleres</span>
      jueves octubre<br>03, 12, 19, 26
    </div>
    <div class="detail detail-time">
      <span class="detail-label">Horario</span>
      5:30pm –8:00pm
    </div>
    <div class="detail detail-place">
      <span class="detail-label">Ubicación</span>
      Cedar Grove Family Resource<br>Center 2250 Alder Way,<br>Fairview CA 90000<br>(555) 014-7413
    </div>
    <p class="note">*Cuidado de niños y cena será proporcionado</p>
  </section>

  <section class="topics">
    <h2>Temas incluyen</h2>
    <ul>
      <li>Llaves para la buena communicación</li>
      <li>Tipos de personalidad y expectativas</li>
      <li>Señales de peligro en una relación</li>
      <li>Técnicas para formar y sostener una relación sana</li>
      <li>Resolucion de problemas</li>
      <li>Como mantener la diversion</li>
      <li>Como adminstrar el dinero entre pareja</li>
      <li>Y muchos mas</li>
    </ul>
  </section>

  <section class="register">
    <p class="register-call">Registración requerida<br>Llámanos hoy!</p>
    <p class="register-info">Para más información llame a<br>Cedar Grove Family Resource Center,<br>(555) 014-7617</p>
  </section>

  <footer class="footer">
    <div class="partner partner-resource"><span class="partner-dot"></span>CEDAR GROVE<br>FAMILY RESOURCE CENTER</div>
    <div class="partner partner-alliance"><span class="partner-dot"></span>Harbor Community Alliance</div>
    <p class="funding">“Funding for this project was provided by the National Family Services Agency, Office for Children and Families, Grant: #00XX0000. These services are available to all eligible persons, regardless of race, gender, age, disability, or religion.”</p>
  </footer>
</main>
</body>
</html>
```